Binary Options Robot Landing Page

I need a landing page for a campaign advertising binary options robot trading. The campaign and overall look and feel should be inspired by this brand: https://quellmarktrader.com/

The screenshots you want to add from the trading area you can simple google. We will replace any screenshots with actual screenshots from our binary trading software.

You can also copy the text since we will replace the text as well.

The name to advertise is "Vextra Pilot - Bright Paths" and will be featured on www.vextrapilot.ws

What is important is the overall look!
- Vextra Pilot
- Clean Design
- Nice colors
- Makes you want to signup and trade!

Target Market(s)

People who wants to earn some extra money by investing and trading options online.

Industry/Entity Type

Advertising

Logo Text

VExtraPilot - Bright Path

Number of Pages Required

1 page

Colors

Designer to choose colors to be used in the design.

Requirements
Must have
• New Logo or remake of current logo
• Design for web resolution
• Design for mobile resolution
• Signup form as attached but designed more flashy!
• The chat popup may not block crucial elements of the design
Nice to have
• Screenshots that makes people interested to signup
• Catchy phrases that will get people interested in the product
• You are allowed to copy or partly copy the current logo
• Design a contact page
Should not have
• US flags

```html
<!DOCTYPE html>
<html lang="en">
<head>
<meta charset="utf-8">
<title>Vextra Pilot - Bright Paths</title>
<link href="https://fonts.googleapis.com/css2?family=Raleway:wght@600;700;800&family=Open+Sans:wght@400;600;700&display=swap" rel="stylesheet">
<style>
:root{
  --blue:#0b4a9b;
  --blue-dark:#0a3f86;
  --green:#5f9e2c;
  --orange:#f26a21;
  --text:#333333;
  --muted:#555555;
  --rule:#e2e2e2;
  --footer:#ededef;
  --white:#ffffff;
}
*{box-sizing:border-box;margin:0;padding:0}
html,body{width:1200px;height:2655px;overflow:hidden;background:var(--white)}
body{font-family:"Open Sans",Arial,sans-serif;color:var(--text)}
.page{position:relative;width:1200px;height:2655px;overflow:hidden}
.abs{position:absolute}
h1,h2,h3,.brand{font-family:"Raleway",Arial,sans-serif}

/* header */
.site-header{position:absolute;left:0;top:0;width:1200px;height:81px;background:var(--white)}
.brand{position:absolute;left:131px;top:22px;font-size:27px;font-weight:800;color:var(--blue);letter-spacing:.3px}
.nav{position:absolute;top:28px;left:0;width:1200px;font-size:13px;color:#222}
.nav a{position:absolute;color:#222;text-decoration:none;line-height:28px;top:0}
.nav .active{background:var(--green);color:var(--white);padding:0 13px;left:568px}
.nav .login{background:var(--orange);color:var(--white);left:990px;width:78px;display:flex;align-items:center;justify-content:center;gap:7px}

/* hero */
.hero{position:absolute;left:0;top:81px;width:1200px;height:523px;
  background:radial-gradient(circle at 900px 230px,#f3e25a 0,#c9b637 70px,#6b6a45 190px,rgba(60,60,62,0) 330px),
  linear-gradient(100deg,#3d4a57 0%,#6a6d72 35%,#4a4a4c 70%,#3a3a3c 100%)}
.signup-card{position:absolute;left:67px;top:154px;width:319px;height:391px;background:var(--white);padding:22px 19px;box-shadow:0 2px 10px rgba(0,0,0,.25)}
.field{height:44px;border:1px solid #cfcfcf;margin-bottom:14px;font-size:12px;color:#222;display:flex;align-items:center;padding-left:17px}
.field.phone{padding:0}
.field.phone .code{width:55px;height:100%;border-right:1px solid #cfcfcf;display:flex;align-items:center;justify-content:center}
.field.phone .num{padding-left:14px}
.open-account{display:block;width:100%;height:51px;margin-top:19px;background:var(--blue);color:var(--white);border:0;font-family:"Open Sans",Arial,sans-serif;font-weight:700;font-size:18px;letter-spacing:.3px}
.hero-title{position:absolute;left:420px;top:398px;font-size:45px;line-height:47px;font-weight:700;color:var(--white);text-shadow:0 2px 6px rgba(0,0,0,.45)}
.slider-dots{position:absolute;left:550px;top:548px;display:flex;gap:17px}
.slider-dots span{width:9px;height:9px;border-radius:50%;background:var(--white)}
.slider-dots span.current{width:12px;height:12px;margin-top:-1.5px;background:transparent;border:2px solid var(--white)}

/* sections */
.section-title{position:absolute;left:0;width:1200px;text-align:center;font-size:23px;font-weight:700;color:var(--blue)}
.section-intro{position:absolute;left:300px;width:600px;text-align:center;font-size:15px;line-height:22px;color:#222}
.rule{position:absolute;left:131px;width:938px;height:1px;background:var(--rule)}
.col{position:absolute;width:300px;text-align:center}
.col h3{font-size:18px;font-weight:700;color:var(--blue);margin-top:18px}
.col p{font-size:13.5px;line-height:21px;color:var(--muted);margin:12px auto 0;width:240px}
.col .icon{height:60px;display:flex;justify-content:center;align-items:flex-end}
.vrule{position:absolute;top:840px;width:1px;height:190px;background:var(--rule)}

.service{position:absolute;width:420px;height:100px}
.service .ring{position:absolute;left:0;top:0;width:100px;height:100px;border:1.5px solid #4f78c4;border-radius:50%;display:flex;align-items:center;justify-content:center}
.service h3{position:absolute;left:126px;top:12px;font-size:18px;font-weight:700;color:var(--blue);white-space:nowrap}
.service p{position:absolute;left:126px;top:46px;width:260px;font-size:13.5px;line-height:21px;color:var(--muted)}
.read-more{position:absolute;left:533px;top:1639px;width:134px;height:39px;border:1.5px solid #4f78c4;display:flex;align-items:center;justify-content:center;gap:10px;font-size:13px;font-weight:700;color:var(--blue)}

.step{position:absolute;width:300px;text-align:center}
.step .icon{height:80px;display:flex;justify-content:center;align-items:flex-end}
.step h3{margin-top:40px;font-size:18px;font-weight:700;color:var(--blue)}
.step p{margin:16px auto 0;width:270px;font-size:13.5px;line-height:22px;color:var(--muted)}

/* footer */
.site-footer{position:absolute;left:0;top:2274px;width:1200px;height:381px;background:var(--footer)}
.footer-brand{position:absolute;left:131px;top:2333px;font-size:27px;font-weight:800;color:var(--blue)}
.follow{position:absolute;left:198px;top:2408px;width:120px;text-align:center;font-size:12px;font-weight:700;color:#111}
.social{position:absolute;left:180px;top:2445px;display:flex;gap:8px}
.social span{width:29px;height:29px;border-radius:50%}
.f-head{position:absolute;top:2333px;font-size:12px;font-weight:700;color:#111}
.menu-list{position:absolute;left:411px;top:2365px;list-style:none;font-size:12px;line-height:24px;color:#333}
.contact-list{position:absolute;left:550px;top:2365px;list-style:none;font-size:12px;color:#333}
.contact-list li{display:flex;gap:17px;line-height:24px}
.contact-list li svg{flex:none;margin-top:7px}
.contact-list .indent{padding-left:27px}
.news-input{position:absolute;left:797px;top:2375px;width:272px;height:45px;background:var(--white);border:1px solid #d4d4d4;display:flex;align-items:center;gap:14px;padding-left:22px;font-size:12px;color:#333}
.signup-btn{position:absolute;left:966px;top:2441px;width:103px;height:34px;background:var(--green);color:var(--white);display:flex;align-items:center;justify-content:center;font-size:14px;font-weight:700}
.footer-rule{position:absolute;left:131px;top:2549px;width:938px;height:1px;background:#cfcfd2}
.copyright{position:absolute;left:0;top:2596px;width:1200px;text-align:center;font-size:11.5px;color:#444}
</style>
</head>
<body>
<div class="page">

  <header class="site-header">
    <div class="brand">VEXTRA PILOT</div>
    <nav class="nav">
      <a class="active">Home</a>
      <a style="left:667px">About us</a>
      <a style="left:758px">FAQ</a>
      <a style="left:818px">Guides</a>
      <a style="left:894px">Contact Us</a>
      <a class="login">
        <svg width="10" height="12" viewBox="0 0 10 12"><rect x="1" y="5" width="8" height="7" fill="#fff"/><path d="M2.5 5V3.5a2.5 2.5 0 0 1 5 0V5" fill="none" stroke="#fff" stroke-width="1.4"/></svg>
        Login
      </a>
    </nav>
  </header>

  <section class="hero" role="img" aria-label="Photo of a businessman holding a glowing golden coin above his open hand, city skyline behind"></section>

  <form class="signup-card">
    <div class="field">First Name</div>
    <div class="field">Last Name</div>
    <div class="field">Valid Email Address</div>
    <div class="field">Choose Password</div>
    <div class="field phone"><span class="code">+357</span><span class="num">Phone No.</span></div>
    <button class="open-account" type="button">OPEN ACCOUNT</button>
  </form>

  <h1 class="hero-title">Vextra Pilot -<br>Bright Paths</h1>
  <div class="slider-dots"><span></span><span class="current"></span><span></span><span></span><span></span></div>

  <!-- welcome -->
  <h2 class="section-title" style="top:657px">WELCOME TO OUR SITE</h2>
  <p class="section-intro" style="top:708px">There are many variations of passages of Lorem Ipsum available, but the majority have suffered alteration in some form, by injected humour, or randomised words which don't look even slightly believable&nbsp; If you are goin</p>

  <div class="col" style="left:107px;top:833px">
    <div class="icon">
      <svg width="60" height="56" viewBox="0 0 60 56"><path d="M30 2 L46 8 V22 C46 32 39 38 30 42 C21 38 14 32 14 22 V8 Z" fill="var(--green)"/><path d="M22 21 L28 27 L38 16" fill="none" stroke="#fff" stroke-width="3.5"/><path d="M2 30 L10 30 L16 44 L26 48 L26 54 L12 54 L2 42 Z M58 30 L50 30 L44 44 L34 48 L34 54 L48 54 L58 42 Z" fill="var(--green)"/></svg>
    </div>
    <h3>Safe &amp; Secure</h3>
    <p>There are many variations of passages of Lorem Ipsum available, but the majority have suffered .</p>
  </div>
  <div class="vrule" style="left:420px"></div>
  <div class="col" style="left:450px;top:833px">
    <div class="icon">
      <svg width="58" height="58" viewBox="0 0 58 58"><circle cx="29" cy="29" r="25" fill="none" stroke="var(--green)" stroke-width="5"/><line x1="12" y1="12" x2="46" y2="46" stroke="var(--green)" stroke-width="5"/></svg>
    </div>
    <h3>No Downloads - No Charges</h3>
    <p>There are many variations of passages of Lorem Ipsum available, but the majority have suffered .</p>
  </div>
  <div class="vrule" style="left:782px"></div>
  <div class="col" style="left:793px;top:833px">
    <div class="icon">
      <svg width="62" height="62" viewBox="0 0 62 62"><polygon points="31,1 36,6 43,4 46,10 53,11 53,18 59,22 56,28 60,34 55,39 56,46 49,48 46,55 39,54 34,60 28,57 22,60 18,54 11,55 9,48 3,45 5,38 1,32 5,26 3,20 9,16 10,9 17,8 21,2 27,5" fill="var(--green)"/><circle cx="31" cy="31" r="19" fill="none" stroke="#fff" stroke-width="2"/><path d="M22 31 L29 38 L41 24" fill="none" stroke="#fff" stroke-width="4"/></svg>
    </div>
    <h3>Trusted Vextra Pilot</h3>
    <p>There are many variations of passages of Lorem Ipsum available, but the majority have suffered .</p>
  </div>

  <div class="rule" style="top:1099px"></div>

  <!-- services -->
  <h2 class="section-title" style="top:1152px">OUR SERVICES</h2>
  <p class="section-intro" style="top:1210px">There are many variations of passages of Lorem Ipsum available, but the majority have suffered alteration in some form, by injected humou.</p>

  <div class="service" style="left:170px;top:1315px">
    <div class="ring"><svg width="40" height="40" viewBox="0 0 40 40"><rect x="3" y="5" width="34" height="22" rx="2" fill="var(--green)"/><rect x="6" y="8" width="28" height="16" fill="#fff"/><path d="M9 21 L16 15 L21 18 L30 11" fill="none" stroke="var(--green)" stroke-width="2.4"/><rect x="16" y="27" width="8" height="6" fill="var(--green)"/><rect x="11" y="33" width="18" height="3" fill="var(--green)"/></svg></div>
    <h3>Free Binary Trading Software</h3>
    <p>There are many variations of passages of Lorem Ipsum availabl.</p>
  </div>
  <div class="service" style="left:644px;top:1315px">
    <div class="ring"><svg width="46" height="46" viewBox="0 0 46 46"><circle cx="15" cy="11" r="7" fill="var(--green)"/><path d="M2 40 C2 26 8 21 15 21 C22 21 28 26 28 40 Z" fill="var(--green)"/><text x="32" y="16" font-family="Open Sans,sans-serif" font-weight="700" font-size="15" fill="var(--green)">$</text><rect x="30" y="32" width="3" height="8" fill="var(--green)"/><rect x="35" y="27" width="3" height="13" fill="var(--green)"/><rect x="40" y="22" width="3" height="18" fill="var(--green)"/></svg></div>
    <h3>Brokers Available</h3>
    <p>There are many variations of passages of Lorem Ipsum availabl.</p>
  </div>
  <div class="service" style="left:170px;top:1471px">
    <div class="ring"><svg width="42" height="30" viewBox="0 0 42 30"><path d="M8 12 V6 H34 V11" fill="none" stroke="var(--green)" stroke-width="4"/><polygon points="28,10 40,10 34,17" fill="var(--green)"/><path d="M34 18 V24 H8 V19" fill="none" stroke="var(--green)" stroke-width="4"/><polygon points="2,20 14,20 8,13" fill="var(--green)"/></svg></div>
    <h3>Sequence</h3>
    <p>There are many variations of passages of Lorem Ipsum availabl.</p>
  </div>
  <div class="service" style="left:644px;top:1471px">
    <div class="ring"><svg width="44" height="44" viewBox="0 0 44 44"><rect x="3" y="19" width="9" height="22" fill="var(--green)"/><path d="M15 20 L22 6 C24 2 29 4 28 9 L26 17 H38 C41 17 43 20 42 23 L38 38 C37 40 35 41 33 41 H15 Z" fill="var(--green)"/></svg></div>
    <h3>Recommended</h3>
    <p>There are many variations of passages of Lorem Ipsum availabl.</p>
  </div>

  <div class="read-more">READ MORE <svg width="6" height="9" viewBox="0 0 6 9"><polygon points="0,0 6,4.5 0,9" fill="var(--blue)"/></svg></div>

  <div class="rule" style="top:1766px"></div>

  <!-- how it works -->
  <h2 class="section-title" style="top:1832px">HOW IT WORKS</h2>
  <p class="section-intro" style="top:1891px">There are many variations of passages of Lorem Ipsum available, but the majority have suffered alteration in some form, by injected humou.</p>

  <div class="step" style="left:108px;top:2005px">
    <div class="icon"><svg width="50" height="80" viewBox="0 0 50 80"><rect x="3" y="4" width="44" height="72" fill="none" stroke="var(--green)" stroke-width="3"/><polygon points="3,4 32,12 32,80 3,76" fill="var(--green)"/><circle cx="26" cy="44" r="2.5" fill="#fff"/></svg></div>
    <h3>Open a free account</h3>
    <p>Contrary to popular belief, Lorem Ipsum is not simply random text.</p>
  </div>
  <svg class="abs" style="left:366px;top:2020px" width="120" height="34" viewBox="0 0 120 34"><path d="M2 22 C35 2 80 2 112 24" fill="none" stroke="#999" stroke-width="1.2"/><path d="M104 18 L113 25 L103 28" fill="none" stroke="#999" stroke-width="1.2"/></svg>
  <div class="step" style="left:450px;top:2005px">
    <div class="icon"><svg width="72" height="66" viewBox="0 0 72 66"><rect x="2" y="2" width="68" height="56" rx="4" fill="var(--green)"/><rect x="9" y="9" width="54" height="42" rx="2" fill="none" stroke="#fff" stroke-width="2"/><circle cx="38" cy="30" r="12" fill="#fff"/><circle cx="38" cy="30" r="6" fill="var(--green)"/><rect x="13" y="20" width="5" height="7" fill="#fff"/><rect x="13" y="33" width="5" height="7" fill="#fff"/><rect x="8" y="58" width="10" height="6" fill="var(--green)"/><rect x="54" y="58" width="10" height="6" fill="var(--green)"/></svg></div>
    <h3>Deposit (no fees!)</h3>
    <p>Contrary to popular belief, Lorem Ipsum is not simply random text.</p>
  </div>
  <svg class="abs" style="left:708px;top:2036px" width="120" height="34" viewBox="0 0 120 34"><path d="M2 14 C35 34 80 32 112 8" fill="none" stroke="#999" stroke-width="1.2"/><path d="M103 7 L113 7 L110 16" fill="none" stroke="#999" stroke-width="1.2"/></svg>
  <div class="step" style="left:792px;top:2005px">
    <div class="icon"><svg width="92" height="84" viewBox="0 0 92 84"><path d="M2 80 H90" stroke="var(--green)" stroke-width="2"/><path d="M8 66 L28 52 L42 58 L62 30 L80 12" fill="none" stroke="var(--green)" stroke-width="2"/><circle cx="80" cy="10" r="4" fill="var(--green)"/><g fill="var(--green)"><rect x="10" y="60" width="5" height="14"/><rect x="19" y="54" width="5" height="20"/><rect x="28" y="58" width="5" height="16"/><rect x="37" y="48" width="5" height="26"/><rect x="46" y="52" width="5" height="22"/><rect x="55" y="36" width="5" height="38"/><rect x="64" y="28" width="5" height="30"/><rect x="73" y="20" width="5" height="38"/></g><g stroke="var(--green)" stroke-width="1.2"><line x1="12.5" y1="56" x2="12.5" y2="78"/><line x1="39.5" y1="44" x2="39.5" y2="78"/><line x1="57.5" y1="32" x2="57.5" y2="78"/><line x1="75.5" y1="16" x2="75.5" y2="62"/></g></svg></div>
    <h3>Begin robot trading!</h3>
    <p>Contrary to popular belief, Lorem Ipsum is not simply random text.</p>
  </div>

  <!-- footer -->
  <footer class="site-footer"></footer>
  <div class="footer-brand">VEXTRA PILOT</div>
  <div class="follow">FOLLOW US</div>
  <div class="social">
    <span style="background:#3b5bab"></span>
    <span style="background:#1da1f2"></span>
    <span style="background:#e9573f"></span>
  </div>

  <div class="f-head" style="left:411px">MENU</div>
  <ul class="menu-list">
    <li>Home</li><li>About us</li><li>FAQ</li><li>Guides</li><li>Contact</li>
  </ul>

  <div class="f-head" style="left:550px">CONTACT US</div>
  <ul class="contact-list">
    <li><svg width="9" height="12" viewBox="0 0 9 12"><path d="M4.5 0 A4.5 4.5 0 0 1 9 4.5 C9 7.5 4.5 12 4.5 12 C4.5 12 0 7.5 0 4.5 A4.5 4.5 0 0 1 4.5 0 Z" fill="#222"/><circle cx="4.5" cy="4.5" r="1.6" fill="#fff"/></svg>47 Larkfield Row</li>
    <li class="indent">Dunmore Heights, CA 90517</li>
    <li><svg width="11" height="11" viewBox="0 0 11 11"><path d="M1 7 A4.5 4.5 0 0 1 10 7" fill="none" stroke="#222" stroke-width="1.6"/><rect x="0" y="6" width="3" height="5" fill="#222"/><rect x="8" y="6" width="3" height="5" fill="#222"/></svg>555.014.927</li>
    <li><svg width="11" height="9" viewBox="0 0 11 9"><rect width="11" height="9" fill="#222"/><path d="M0 0 L5.5 5 L11 0" fill="none" stroke="#fff" stroke-width="1"/></svg>info@vextrapilot.ws</li>
  </ul>

  <div class="f-head" style="left:797px">NEWSLETTER SIGNUP</div>
  <div class="news-input"><svg width="11" height="9" viewBox="0 0 11 9"><rect width="11" height="9" fill="#222"/><path d="M0 0 L5.5 5 L11 0" fill="none" stroke="#fff" stroke-width="1"/></svg>E mail id</div>
  <div class="signup-btn">SIGNUP!</div>

  <div class="footer-rule"></div>
  <div class="copyright">Copyrights @ 2017 All Rights Reserved</div>

</div>
</body>
</html>
```